Business Landing Page for SEO Company

Need the landing page of the website designed - I will provide the copy, will need to include details of my company and the services offered, about us, testimonials, faq, etc., and all these elements will need to be arranged graphically on the page.

I want something similar to this: https://plorvantix.com/

Not in terms of color or theme or anything, but we offer a similar service and want to display similar information.

Th services we provide are:

Premium Links
Monthly Links Subscription
Link Insertions

Need to advertise them on the front page. Additionally need a place for testimonials, company details, etc.,

We already have logo for the website. Please use the attached file to insert the logo within the overal design.
Updates

Target Market(s)

SEO marketers and agencies

Number of Pages Required

1 page

```html
<!DOCTYPE html>
<html lang="en">
<head>
<meta charset="utf-8">
<title>Quellmark – Link Building Service</title>
<link href="https://fonts.googleapis.com/css2?family=Montserrat:ital,wght@0,400;0,500;0,600;0,700;0,800;1,400;1,500&display=swap" rel="stylesheet">
<style>
:root{
  --ink:#0d0d0e;
  --card:#121213;
  --line:#2c2c2e;
  --white:#ffffff;
  --orange:#ff7a00;
  --coral:#f2643a;
  --blue:#1f73c9;
  --blue-bright:#2b8be6;
  --sky:#ddeefd;
  --text:#3a3a3a;
  --muted:#8a8f98;
}
*{box-sizing:border-box;margin:0;padding:0}
html,body{width:1200px;height:3704px;overflow:hidden}
body{position:relative;font-family:'Montserrat',sans-serif;background:var(--white);color:var(--text)}
.abs{position:absolute}
.bg-shapes{position:absolute;left:0;top:0}

/* nav */
.brand{left:150px;top:30px;display:flex;align-items:center;gap:10px;font-size:26px;font-weight:600;color:var(--white)}
.brand-dot{width:12px;height:12px;border-radius:50%;background:var(--coral)}
.nav{top:36px;left:588px;display:flex;gap:34px;font-size:13px;font-weight:500;color:var(--white)}
.nav .active{color:#4f9be6;border-bottom:1px solid #4f9be6;padding-bottom:3px}
.nav-cta{left:931px;top:26px;width:118px;height:37px;border-radius:19px;background:var(--coral);color:var(--white);font-size:12.5px;font-weight:600;display:flex;align-items:center;justify-content:center}

/* hero */
.hero-kicker{top:148px;width:1200px;text-align:center;color:var(--white);font-size:24px;font-weight:700}
.hero-title{top:182px;width:1200px;text-align:center;color:var(--white);font-size:46px;font-weight:800;letter-spacing:.5px}
.hero-copy{top:257px;left:200px;width:800px;text-align:center;color:var(--white);font-size:16px;font-weight:500;line-height:30px}

/* service cards */
.service{top:434px;width:286px;height:438px;background:var(--card);border:1px solid var(--line);border-radius:4px;text-align:center;color:var(--white)}
.service svg{margin-top:42px}
.service h3{margin-top:22px;font-size:17px;font-weight:700}
.service .dash{width:30px;height:2px;background:var(--white);margin:28px auto 0}
.service p{margin:26px auto 0;width:270px;font-size:12.5px;line-height:22.5px}
.service .btn{position:absolute;left:68px;bottom:45px;width:150px;height:48px;border-radius:24px;background:#efefef;color:#222;font-size:12.5px;font-weight:600;display:flex;align-items:center;justify-content:center}
.service .btn.hot{background:var(--orange);color:var(--white)}

/* about */
.about-art{left:165px;top:984px;width:381px;height:281px;border-radius:8px;background:linear-gradient(160deg,#eef2fa,#d9e2f7 60%,#f3f4f7)}
.section-title{font-size:31px;font-weight:800;color:#111}
.underline{height:3px;width:30px;background:var(--blue)}
.about-title{left:578px;top:956px}
.about-line{left:578px;top:1009px}
.about-copy{left:578px;top:1040px;width:480px;font-size:12.5px;line-height:25.5px;color:#333;white-space:nowrap}
.btn-blue{background:var(--blue);color:var(--white);font-size:12.5px;font-weight:600;display:flex;align-items:center;justify-content:center;border-radius:3px}
.about-btn{left:578px;top:1250px;width:119px;height:38px}

/* testimonials */
.testimonials{left:0;top:1377px;width:1200px;height:533px;background:var(--sky)}
.center-title{width:1200px;text-align:center;font-size:26px;font-weight:800;color:#111}
.center-line{left:585px}
.center-sub{width:1200px;text-align:center;font-size:11px;color:var(--muted)}
.quote{top:1581px;width:278px;height:116px;background:var(--white);border:1px solid #c9ccd2;font-style:italic;color:#8c8c8c;font-size:13px;line-height:19px;text-align:center;padding:20px 0 0;white-space:nowrap}
.qmark{position:absolute;top:8px;font-size:30px;font-weight:800;font-style:normal;line-height:1}
.qmark.l{left:12px;color:var(--coral)}
.qmark.r{right:12px;color:var(--blue)}
.person{top:1713px;display:flex;align-items:center;gap:14px}
.avatar{width:60px;height:60px;border-radius:50%;background:linear-gradient(135deg,#b9a48e,#5d4c42)}
.person b{display:block;font-size:12.5px;font-weight:600;color:#111}
.person span{font-size:10.5px;color:var(--blue)}
.dot{top:1810px;width:10px;height:10px;border-radius:50%;background:#6fa6e0}
.dot.on{background:var(--blue)}

/* faq */
.faq-q{height:60px;background:var(--ink);color:var(--white);font-size:16px;font-weight:500;display:flex;align-items:center;padding-left:28px;width:428px}
.faq-q .label{position:relative;z-index:1}
.faq-q i{position:absolute;right:22px;font-style:normal;font-size:16px}
.faq-q .bubble{position:absolute;right:55px;top:6px;width:66px;height:48px;border-radius:50%;border:3px solid #1f1f21}
.faq-a{left:150px;top:2174px;width:428px;height:161px;background:var(--sky);box-shadow:0 2px 8px rgba(0,0,0,.25);font-size:12.5px;line-height:22.5px;color:#333;padding:22px 28px;white-space:nowrap}
.more-btn{left:533px;top:2470px;width:134px;height:38px}

/* contact */
.contact{left:0;top:2598px;width:1200px;height:820px;background:linear-gradient(90deg,#2b63ab 0%,#4b5f94 35%,#8b5a62 65%,#c4532b 100%)}
.contact-title{top:2680px;color:var(--white)}
.field{background:rgba(255,255,255,.9);font-size:12px;font-style:italic;color:#666;padding:14px 28px;letter-spacing:.5px}
.submit{left:217px;top:3077px;width:765px;height:43px;background:var(--blue-bright);color:var(--white);font-size:11.5px;font-weight:700;letter-spacing:.5px;display:flex;align-items:center;justify-content:center;gap:8px;border-radius:2px}

/* footer */
.f-head{top:3351px;font-size:13px;font-weight:700;color:var(--white)}
.f-line{top:3374px;width:22px;height:2px;background:var(--blue-bright)}
.f-text{color:#c8c8c8;font-size:12.5px;line-height:22.5px;white-space:nowrap}
.f-list{list-style:none;color:#a9a9ad;font-size:12.5px}
.f-list li{height:36px}
.email{left:831px;top:3457px;width:172px;height:38px;background:#2b2b2e;border-radius:3px 0 0 3px;color:#999;font-size:12px;font-style:italic;padding:12px 18px}
.email-btn{left:1003px;top:3457px;width:47px;height:38px;background:var(--blue-bright);border-radius:0 3px 3px 0;display:flex;align-items:center;justify-content:center}
.social{top:3526px;width:27px;height:27px;border-radius:50%;background:#2b2b2e}
.social.first{background:var(--white)}
.rule{left:150px;top:3646px;width:900px;height:1px;background:#2c2c2e}
.legal{top:3668px;font-size:9px;color:#9a9aa0}
.legal-links{top:3668px;right:150px;display:flex;gap:14px;font-size:9px;color:#9a9aa0}
</style>
</head>
<body>

<svg class="bg-shapes" width="1200" height="3704" aria-hidden="true">
  <rect x="0" y="0" width="1200" height="620" fill="#0d0d0e"/>
  <path d="M0 525 Q600 700 1200 525 V590 Q600 710 0 590 Z" fill="#1f73c9"/>
  <path d="M0 590 Q600 710 1200 590 V800 H0 Z" fill="#ffffff"/>
  <rect x="0" y="0" width="1200" height="2" fill="#1f73c9"/>
</svg>

<div class="abs brand"><span class="brand-dot"></span>Quellmark</div>
<nav class="abs nav"><span class="active">Services</span><span>About Us</span><span>Testimonials</span><span>Faq</span></nav>
<div class="abs nav-cta">Contact Us</div>

<div class="abs hero-kicker">THE LEADER OF THE MARKET</div>
<h1 class="abs hero-title">BUILDING SERVICE</h1>
<p class="abs hero-copy">Lorem ipsum dolor sit amet, consectetur adipiscing elit, sed do eiusmod tempor<br>incididunt ut labore et dolore magna aliqua. Ut enim ad minim veniam, quis nostrud<br>exercitation ullamco laboris nisi ut aliquip ex ea commodo consequat. Duis aute irure<br>dolor in reprehenderit in voluptate velit esse cillum.</p>

<div class="abs service" style="left:150px">
  <svg width="40" height="40" viewBox="0 0 24 24" fill="none" stroke="#ff7a00" stroke-width="3" stroke-linecap="round"><path d="M10 14a4 4 0 0 0 5.7 0l3-3a4 4 0 0 0-5.7-5.7l-1 1"/><path d="M14 10a4 4 0 0 0-5.7 0l-3 3a4 4 0 0 0 5.7 5.7l1-1"/></svg>
  <h3>Premium Links</h3><div class="dash"></div>
  <p>Sed ut perspiciatis unde omnis<br>iste natus error sit voluptatem<br>accusantium doloremque<br>perspiciatis unde omnis iste<br>natus error sit voluptatem.</p>
  <div class="btn">View Options</div>
</div>
<div class="abs service" style="left:457px">
  <svg width="40" height="40" viewBox="0 0 24 24" fill="none" stroke="#ff7a00" stroke-width="3" stroke-linecap="round"><path d="M10 14a4 4 0 0 0 5.7 0l3-3a4 4 0 0 0-5.7-5.7l-1 1"/><path d="M14 10a4 4 0 0 0-5.7 0l-3 3a4 4 0 0 0 5.7 5.7l1-1"/></svg>
  <h3>Monthly Links Subscription</h3><div class="dash"></div>
  <p>Consectetur, adipisci velit, sed<br>quia non numquam eius modi<br>tempora incidunt ut labore et<br>dolore magnam aliquam quaerat<br>voluptatem numquam.</p>
  <div class="btn hot">View Options</div>
</div>
<div class="abs service" style="left:765px">
  <svg width="40" height="40" viewBox="0 0 24 24" fill="none" stroke="#ff7a00" stroke-width="3" stroke-linecap="round"><path d="M10 14a4 4 0 0 0 5.7 0l3-3a4 4 0 0 0-5.7-5.7l-1 1"/><path d="M14 10a4 4 0 0 0-5.7 0l-3 3a4 4 0 0 0 5.7 5.7l1-1"/></svg>
  <h3>Link Insertions</h3><div class="dash"></div>
  <p>Lorem ipsum dolor sit amet, con-<br>sectetur adipiscing elit, sed do<br>eiusmod tempor incididunt ut<br>labore et dolore magna aliqua. Ut<br>enim ad minim veniam.</p>
  <div class="btn">View Options</div>
</div>

<div class="abs about-art" role="img" aria-label="Illustration of a woman examining a web dashboard through a large magnifying glass"></div>
<h2 class="abs section-title about-title">About Us</h2>
<div class="abs underline about-line"></div>
<p class="abs about-copy">Lorem ipsum dolor sit amet, consectetur adipiscing elit, sed do eiusmod<br>tempor incididunt ut labore et dolore magna aliqua. Ut enim ad minim<br>veniam, quis nostrud exercitation ullamco laboris nisi ut aliquip ex ea<br>commodo consequat. Duis aute irure dolor in reprehenderit in voluptate<br>velit esse cillum dolore eu fugiat nulla pariatur. Excepteur sint occaecat<br>cupidatat non proident, sunt in culpa qui officia deserunt mollit anim id<br>est laborum magni dolores eos qui ratione.</p>
<div class="abs btn-blue about-btn">Learn More</div>

<section class="abs testimonials"></section>
<h2 class="abs center-title" style="top:1461px">Our Testimonials</h2>
<div class="abs underline center-line" style="top:1508px"></div>
<p class="abs center-sub" style="top:1530px">See what our lovely customers saying about working with us.</p>

<div class="abs quote" style="left:150px"><span class="qmark l">“</span><span class="qmark r">”</span>Lorem ipsum dolor sit<br>consctetur adipiscing elit. Se<br>Integer lore quam, adipiscing in<br>condimentum tristique vel,</div>
<div class="abs quote" style="left:461px"><span class="qmark l">“</span><span class="qmark r">”</span>Lorem ipsum dolor sit<br>consctetur adipiscing elit. Se<br>Integer lore quam, adipiscing in<br>condimentum tristique vel,</div>
<div class="abs quote" style="left:772px"><span class="qmark l">“</span><span class="qmark r">”</span>Lorem ipsum dolor sit<br>consctetur adipiscing elit. Se<br>Integer lore quam, adipiscing in<br>condimentum tristique vel,</div>

<div class="abs person" style="left:215px"><div class="avatar" role="img" aria-label="Client portrait photo"></div><div><b>Owen Marsh</b><span>Business Owner</span></div></div>
<div class="abs person" style="left:526px"><div class="avatar" role="img" aria-label="Client portrait photo"></div><div><b>Mira Dalton</b><span>Business Owner</span></div></div>
<div class="abs person" style="left:837px"><div class="avatar" role="img" aria-label="Client portrait photo"></div><div><b>Ravi Kellan</b><span>Business Owner</span></div></div>

<div class="abs dot" style="left:576px"></div>
<div class="abs dot on" style="left:595px"></div>
<div class="abs dot" style="left:614px"></div>

<h2 class="abs center-title" style="top:1993px">Frequently Asked Questions</h2>
<div class="abs underline center-line" style="top:2041px"></div>
<p class="abs center-sub" style="top:2065px">Find the answers to your questions</p>

<div class="abs faq-q" style="left:150px;top:2114px"><span class="bubble"></span><span class="label">How to work with us?</span><i>+</i></div>
<div class="abs faq-a">Lorem ipsum dolor sit amet, consectetur adipiscing elit, sed<br>do eiusmod tempor incididunt ut labore et dolore magna<br>aliqua. Ut enim ad minim veniam, quis nostrud exercitation<br>ullamc laboris nisi ut aliquip ex ea commodo consequat.<br>Duis aute irure dolor in reprehenderit.</div>
<div class="abs faq-q" style="left:150px;top:2373px"><span class="bubble"></span><span class="label">How to get premium links?</span><i>+</i></div>
<div class="abs faq-q" style="left:622px;top:2114px"><span class="bubble"></span><span class="label">How long it takes to see results?</span><i>+</i></div>
<div class="abs faq-q" style="left:622px;top:2219px"><span class="bubble"></span><span class="label">How does it works?</span><i>+</i></div>
<div class="abs faq-q" style="left:622px;top:2324px"><span class="bubble"></span><span class="label">How to get a monthly subscription?</span><i>+</i></div>
<div class="abs btn-blue more-btn">More Questions</div>

<section class="abs contact"></section>
<h2 class="abs center-title contact-title">Contact Us</h2>
<div class="abs center-line" style="top:2727px;width:30px;height:3px;background:#fff"></div>
<p class="abs center-sub" style="top:2749px;color:#fff">Feel free to contact us for any inquiry</p>
<div class="abs field" style="left:217px;top:2799px;width:375px;height:44px">Your Name</div>
<div class="abs field" style="left:608px;top:2799px;width:374px;height:44px">Your Email</div>
<div class="abs field" style="left:217px;top:2860px;width:375px;height:43px">Your Phone</div>
<div class="abs field" style="left:608px;top:2860px;width:374px;height:43px">Project Type</div>
<div class="abs field" style="left:217px;top:2919px;width:765px;height:135px">Your Message</div>
<div class="abs submit">Submit Message <svg width="11" height="11" viewBox="0 0 24 24" fill="#fff"><path d="M22 2 2 10l7 3 3 7z"/></svg></div>

<svg class="bg-shapes" style="top:3100px" width="1200" height="604" aria-hidden="true">
  <path d="M0 200 Q600 18 1200 200 V604 H0 Z" fill="#f2643a"/>
  <path d="M0 225 Q600 55 1200 225 V604 H0 Z" fill="#0d0d0e"/>
</svg>

<div class="abs f-head" style="left:150px">About Your Company</div>
<p class="abs f-text" style="left:150px;top:3396px">Lorem ipsum dolor sit amet, consectetur<br>adipiscing elit, sed do eiusmod tempor<br>incididunt ut labore et dolore magna<br>aliqua. Ut enim ad minim veniam, quis<br>nostrud exercitation ullamco.</p>
<div class="abs" style="left:150px;top:3535px;font-size:12px;font-weight:600;color:#fff">Give us a Call</div>
<div class="abs" style="left:150px;top:3553px;font-size:18px;font-weight:500;color:var(--blue-bright)">123 456 7890</div>

<div class="abs f-head" style="left:516px">Menu</div><div class="abs f-line" style="left:516px"></div>
<ul class="abs f-list" style="left:516px;top:3400px"><li>Services</li><li style="position:relative"><span style="position:absolute;left:-15px;color:var(--blue-bright)">»</span>About Us</li><li>Testimonials</li><li>FAQ</li><li>Contact Us</li></ul>
<div class="abs f-head" style="left:642px">Services</div><div class="abs f-line" style="left:642px"></div>
<ul class="abs f-list" style="left:642px;top:3400px"><li>Premium Links</li><li>Monthly link Subscription</li><li>Link Insertions</li></ul>
<div class="abs f-head" style="left:831px">Subscribe</div><div class="abs f-line" style="left:831px"></div>
<p class="abs f-text" style="left:831px;top:3398px;color:#a9a9ad;line-height:20px">Signup to our email list and get<br>latest updates and news.</p>
<div class="abs email">Email Address</div>
<div class="abs email-btn"><svg width="16" height="12" viewBox="0 0 16 12" fill="none" stroke="#fff" stroke-width="1.5"><rect x="1" y="1" width="14" height="10" rx="1"/><path d="M1 2l7 5 7-5"/></svg></div>
<div class="abs social first" style="left:832px"></div>
<div class="abs social" style="left:874px"></div>
<div class="abs social" style="left:916px"></div>
<div class="abs social" style="left:957px"></div>

<div class="abs rule"></div>
<div class="abs legal" style="left:150px">Copyright © Business Name 2021 All Rights Reserved.</div>
<div class="abs legal-links"><span>Terms &amp; Conditions</span><span style="color:#fff">Privacy</span><span>Policy</span><span>Testimonials</span><span>Faq</span></div>

</body>
</html>
```